Graphic for The Quill newsletter - Graffiti style font

I need a few different images that have different purposes but are all for an email newsletter I produce, The Quill. One is for social media posting and the other is for use in the newsletter itself as the banner (you can see the front page of the newsletter attached to get a feel for how it has existed to date) and on my website to take people to current and back issues of the newsletter. The Quill is a monthly newsletter with updates on the real estate market in Hudson Valley, New York. Social media postings will be to advertise the newsletter and organically grow with new subscribers. The Quill got its name due to the Hudson Valley being steeped in brickyard history as much of construction in yesteryear was of brick with the Hudson Valley being a center point of manufacture.
1). Image of bricks (like a brick wall) with the words "The Quill". My vision is The Quill image would be of more vintage looking brick wall with the words "The Quill" in almost a hand written graffiti type of font potentially on a slant. I need this as a jpg file that is sized to post on Instagram, Facebook and LinkedIn. The purpose of this one is to catch eye and lead people to click to subscribe.
2) I also need a second banner image for the website and email newsletter that has the same feel but includes "Hudson Valley Real Estate News and Views". If "Hudson Valley Real Estate News and Views" can also fit on the one for social media posting, it would be ideal, but I would opt to exclude the extra words rather than clutter on social media if need be. For the newsletter banner version, I have attached a copy of the last Quill newsletter that went out. I'm looking to replace the current words "The Quill" with an actual image for the next newsletter.
I attached my logo so you can get a feel for the colors. It can contrast with the logo to stand out but it needs to be a complimentary contrast with the colors in the logo so it works in close proximity to it in the newsletter (as you'll see in attached). While it would be ideal to have consistency across platforms, the version for social media can utilize a different color theme if desired as that image will stand alone without proximity to my logo.
Target Market(s)
35-65 male and female
Other font styles liked:
- more on the graffiti side
Requirements
Must have
- Quill wall as backdrop and handwritten on the graffiti style font. For newsletter and website banner it can't clash with my logo as they would be in close proximity of each other. It can complimentary contrast though.
Nice to have
- "Hudson Valley Real Estate News and Views" included as a tagline and descriptor . Along the lines of the attached font, but not. More bold. Less whimsical and more on the graffiti side.

```html
<!DOCTYPE html>
<html lang="en">
<head>
<meta charset="utf-8">
<title>The Quill – Newsletter Banner</title>
<link rel="stylesheet" href="https://fonts.googleapis.com/css2?family=Kaushan+Script&display=swap">
<style>
  :root {
    --brick-deep: #a8593b;
    --brick-mid: #c07a58;
    --brick-light: #cf9b7c;
    --mortar: #cdb9a0;
    --paint-white: #ffffff;
  }

  html, body {
    margin: 0;
    padding: 0;
    width: 1200px;
    height: 400px;
    overflow: hidden;
    background: var(--mortar);
  }

  .banner {
    position: relative;
    width: 1200px;
    height: 400px;
    overflow: hidden;
  }

  .banner__wall {
    position: absolute;
    inset: 0;
    background:
      radial-gradient(ellipse at 25% 40%, var(--brick-light) 0%, transparent 55%),
      radial-gradient(ellipse at 80% 70%, var(--brick-deep) 0%, transparent 60%),
      linear-gradient(180deg, var(--brick-mid) 0%, var(--mortar) 50%, var(--brick-mid) 100%);
  }

  .banner__title {
    position: absolute;
    left: 0;
    right: 0;
    top: 50%;
    margin: 0;
    transform: translateY(-56%) rotate(-4deg);
    text-align: center;
    font-family: "Kaushan Script", cursive;
    font-weight: 400;
    font-size: 215px;
    line-height: 1;
    letter-spacing: 2px;
    color: var(--paint-white);
    white-space: nowrap;
  }
</style>
</head>
<body>
  <main class="banner">
    <div class="banner__wall" role="img" aria-label="Weathered vintage red brick wall with pale mortar"></div>
    <h1 class="banner__title">The Quill</h1>
  </main>
</body>
</html>
```